Pitch book for the 2025 K7R Global Skycup event in Muncie, Indiana, USA

Title: Fueling the Future of Aeromodeling: Sponsor the 2025 K7R Global Skycup
1. Event Overview
What: The 2025 ORV K7R Global Skycup for Aerobatic Model Aircraft.
When: August 9–16, 2025.
Where: Institute for Scale Flightcraft (ISF) Headquarters, Muncie, Indiana.
Hosted by: Institute for Scale Flightcraft (ISF) in partnership with the Federated Guild for Remote Stunt Piloting (FGRSP).
Participants: Top pilots from across the globe, including juniors and female competitors.
2. Why Sponsor?
Shaping the Future Workforce: Inspire youth to explore careers in aerospace, aviation, and unmanned systems (drones, RPVs), bridging hobbies and high-tech industries like Corvane, Halbrook Teller, and more.
Brand Visibility: Engage with a global audience of enthusiasts, professionals, and media at a premier international event.
Community Impact: Support an event that promotes innovation, STEM education, and cultural exchange.
3. Key Features of the Event
Cutting-Edge Venue: Over 1,100 acres of flying space tailored for precision aerobatics.
Diverse Competitions: Featuring junior and female classifications alongside world-class competitors.
Global Audience: Media coverage, live streams, and on-site spectators.
4. Sponsorship Opportunities
Title Sponsor ($50,000):
Naming rights: "Your Brand Presents the 2025 K7R Global Skycup."
Logo placement on all event materials, website, and livestreams.
Prime exhibit space at the venue.
Gold Sponsor ($25,000):
Prominent branding on materials and media.
Speaking opportunity at the opening or closing ceremony.
Silver Sponsor ($10,000):
Recognition in event communications.
Inclusion in the sponsor wall at the venue.
Event Sponsor ($5,000):
Branding on specific activities (e.g., banquet, practice days).
Custom Sponsorships: Tailored to fit corporate goals, including STEM outreach and branded giveaways.
5. Audience Demographics
Competitors: Over 100 elite pilots from 40+ countries.
Spectators & Supporters: Thousands of attendees, ranging from hobbyists to industry professionals.
Media Reach: Coverage by international aeromodelling and aerospace outlets.
6. STEM and Industry Connections
Showcase pathways from aeromodelling to careers in aviation, engineering, and defense.
Collaborate with sponsors on outreach programs for local schools and universities.
7. Marketing Benefits
Digital: Inclusion in newsletters, website, and social media campaigns.
On-Site Branding: Banners, booths, and branded giveaways.
Networking: Access to high-value attendees and industry leaders.
8. Budget Breakdown
Goal: Raise $180,000 to support the championship.
Funding Allocation:
$70,000: Event logistics (venue, staff, equipment).
$50,000: Participant support (travel subsidies, junior competitor outreach).
$30,000: Marketing and media coverage.
$20,000: Amenities and hospitality.
9. Call to Action
Be Part of the Legacy: Join us in creating a memorable event that not only crowns world champions but also inspires future innovators.
Contact Information:
Name: [Your Name]
Email: [Your Email]
Phone: [Your Phone]
Website: [Event Website Link]

```html
<!DOCTYPE html>
<html lang="en">
<head>
<meta charset="utf-8">
<title>2025 K7R Global Skycup – Sponsorship Pitch Book</title>
<link rel="stylesheet" href="https://fonts.googleapis.com/css2?family=Archivo+Black&family=Barlow:ital,wght@0,400;0,800;1,400&family=Barlow+Condensed:wght@600;700;800&family=Barlow+Semi+Condensed:ital,wght@0,300;0,400;0,500;0,600;1,300;1,400&family=Inter:wght@300;400&display=swap">
<style>
:root{
  --ink:#231f20;
  --red:#b23f2e;
  --navy:#1b2f5c;
  --white:#ffffff;
  --paper:#ffffff;
  --sky:#6f9fd6;
  --field:#8a8560;
}
*{margin:0;padding:0;box-sizing:border-box}
html,body{width:849px;height:1200px;overflow:hidden;background:var(--paper)}
body{position:relative;font-family:"Barlow Semi Condensed",sans-serif;color:var(--white)}
.spread{position:absolute;width:613px;height:474px;background:var(--ink);overflow:hidden}
.spread--outside{left:117px;top:78px}
.spread--inside{left:119px;top:648px}
.abs{position:absolute}
.photo{position:absolute}

/* outside spread */
.tiers-title{left:20px;top:31px;font-family:"Barlow",sans-serif;font-weight:800;font-size:13.5px;letter-spacing:-0.2px}
.tier{position:absolute;left:31px;width:170px}
.tier h3{font-weight:500;font-size:9.8px;letter-spacing:0.1px}
.tier ul{margin-top:2px;padding-left:16px;font-weight:300;font-size:8.4px;line-height:11.6px}
.tier li::marker{font-size:7px}
.divider{position:absolute;left:31px;width:34px;height:2px;background:var(--red)}
.custom{left:20px;top:378px;width:160px}
.custom h3{font-weight:500;font-size:9.8px}
.custom p{margin-top:11px;font-style:italic;font-weight:300;font-size:8.4px;line-height:11.6px;text-align:justify}
.join{left:226px;top:152px;width:52px;height:183px}
.join span{position:absolute;left:50%;top:50%;width:183px;transform:translate(-50%,-50%) rotate(-90deg);font-family:"Archivo Black",sans-serif;font-size:19.5px;line-height:23px;text-align:left}
.rule{height:2px;background:var(--red)}
.lead{left:222px;top:363px;width:170px;font-family:"Inter",sans-serif;font-weight:300;font-size:8px;line-height:11.6px}
.contact{left:243px;font-family:"Inter",sans-serif;font-weight:300;font-size:8.4px;display:flex;align-items:center;gap:9px}
.contact svg{width:10px;height:10px}
.cover-block{left:453px;top:89px;width:160px;height:157px;background:var(--navy)}
.cover-title{left:468px;top:126px;width:140px;font-family:"Barlow Condensed",sans-serif;font-weight:800;font-size:14.2px;line-height:13.8px;text-transform:uppercase}
.date-box{left:441px;top:202px;width:142px;height:49px;background:var(--red);padding:9px 0 0 27px;font-family:"Barlow Condensed",sans-serif;font-weight:600;font-size:10px;line-height:11px;text-transform:uppercase}
.event-mark{left:419px;top:30px;width:45px;font-family:"Barlow Condensed",sans-serif;font-weight:800;font-size:6.5px;line-height:7px;color:var(--white);text-align:center;display:flex;flex-direction:column;align-items:center;gap:2px}
.event-mark i{display:block;width:8px;height:8px;border-radius:50%;background:var(--red)}
.partner-strip{left:474px;top:439px;width:139px;height:35px;background:var(--white)}
.partner-corner{left:576px;top:351px;width:37px;height:88px;background:var(--white)}
.partners{left:487px;top:453px;width:116px;display:flex;justify-content:space-between;font-family:"Barlow Condensed",sans-serif;font-weight:700;font-size:7px;color:var(--navy)}

/* inside spread */
.intro-block{left:0;top:0;width:186px;height:118px;background:var(--navy)}
.tagline{left:20px;top:44px;width:152px;font-style:italic;font-weight:300;font-size:8.4px;line-height:11.6px;text-align:justify}
.heading-box{background:var(--red)}
.overview-box{left:20px;top:74px;width:184px;height:64px;padding:16px 0 0 10px}
.panel-heading{font-weight:500;font-size:24px;line-height:24px}
.overview-list{left:41px;top:150px;width:150px;padding-left:9px;font-weight:300;font-size:8.4px;line-height:14px}
.overview-list b,.feature-list b{font-weight:600}
.why-title{left:223px;top:105px;font-family:"Archivo Black",sans-serif;font-size:19px}
.why{left:230px;width:160px}
.why h3{font-weight:500;font-size:9.6px}
.why p{font-weight:300;font-size:8.4px;line-height:11.6px;text-align:justify}
.why-note{left:223px;top:402px;width:160px;font-style:italic;font-weight:300;font-size:8.4px;line-height:11.6px}
.red-foot{left:205px;top:427px;width:205px;height:47px;background:var(--red)}
.features-box{left:422px;top:82px;width:191px;height:71px;background:rgba(178,63,46,.93);padding:6px 0 0 10px}
.feature-list{left:444px;top:168px;width:144px;padding-left:0;font-weight:300;font-size:8.4px;line-height:11.6px;text-align:justify}
.stem-block{left:409px;top:286px;width:204px;height:188px;background:var(--navy)}
.stem-title{left:428px;top:294px;font-weight:500;font-size:19.5px;line-height:23px}
.stem-list{left:447px;top:362px;width:143px;font-weight:300;font-size:8.4px;line-height:11.6px;text-align:justify}
.stem-note{left:439px;top:443px;width:157px;font-style:italic;font-weight:300;font-size:8.4px;line-height:11.6px;text-align:justify}
ul.dots{list-style:disc}
ul.dots li::marker{font-size:7px}
</style>
</head>
<body>

<!-- Outside spread -->
<section class="spread spread--outside">
  <h2 class="abs tiers-title">Sponsorship Opportunities</h2>

  <div class="tier" style="top:65px">
    <h3>TITLE SPONSOR ($50,000):</h3>
    <ul>
      <li>Naming rights: "Your Brand Presents the 2025 K7R Global Skycup."</li>
      <li>Logo placement on event materials, website, and livestreams.</li>
      <li>Prime exhibit space at the venue.</li>
    </ul>
  </div>
  <div class="divider" style="top:152px"></div>

  <div class="tier" style="top:171px">
    <h3>GOLD SPONSOR ($25,000):</h3>
    <ul>
      <li>Prominent branding on materials and media.</li>
      <li>Speaking opportunity at the opening or closing ceremony.</li>
    </ul>
  </div>
  <div class="divider" style="top:235px"></div>

  <div class="tier" style="top:254px;width:190px">
    <h3>SILVER SPONSOR ($10,000):</h3>
    <ul>
      <li>Recognition in event communications.</li>
      <li>Inclusion in the sponsor wall at the venue.</li>
    </ul>
  </div>
  <div class="divider" style="top:295px"></div>

  <div class="tier" style="top:313px">
    <h3>EVENT SPONSOR ($5,000):</h3>
    <ul>
      <li>Branding on specific activities (e.g., banquet, practice days).</li>
    </ul>
  </div>

  <div class="abs custom">
    <h3>CUSTOM SPONSORSHIPS:</h3>
    <p>Tailored packages for STEM outreach or branded giveaways.<br>Choose the sponsorship level that aligns with your corporate goals.</p>
  </div>

  <div class="abs join"><span>Join Us in Making History!</span></div>

  <div class="photo" role="img" aria-label="Pilots standing beside an aerobatic model plane at the flying field" style="left:288px;top:0;width:121px;height:356px;background:linear-gradient(180deg,#4f86cc 0%,#8db4e0 45%,#d9dde0 62%,#7a7655 100%)"></div>
  <div class="abs rule" style="left:222px;top:355px;width:187px"></div>

  <p class="abs lead">Be part of an event that crowns world champions and inspires future innovators.</p>

  <div class="abs contact" style="top:401px">
    <svg viewBox="0 0 24 24" aria-hidden="true"><path fill="#fff" d="M6.6 10.8a15 15 0 0 0 6.6 6.6l2.2-2.2c.3-.3.7-.4 1-.2 1.1.4 2.3.6 3.6.6.6 0 1 .4 1 1V20c0 .6-.4 1-1 1A17 17 0 0 1 3 4c0-.6.4-1 1-1h3.5c.6 0 1 .4 1 1 0 1.3.2 2.5.6 3.6.1.3 0 .7-.2 1z"/></svg>
    <span>+123-4567-890</span>
  </div>
  <div class="abs contact" style="top:418px">
    <svg viewBox="0 0 24 24" aria-hidden="true"><circle cx="12" cy="12" r="10" fill="none" stroke="#fff" stroke-width="2"/><path fill="none" stroke="#fff" stroke-width="1.6" d="M2 12h20M12 2c3 3 3 17 0 20M12 2c-3 3-3 17 0 20"/></svg>
    <span>www.website.com</span>
  </div>
  <div class="abs contact" style="top:434px">
    <svg viewBox="0 0 24 24" aria-hidden="true"><rect x="2" y="5" width="20" height="14" fill="#fff"/><path d="M2 5l10 8 10-8" fill="none" stroke="#231f20" stroke-width="2"/></svg>
    <span>hello@email.com</span>
  </div>

  <div class="photo" role="img" aria-label="Podium ceremony with competitors and national flags against a blue sky" style="left:409px;top:0;width:167px;height:439px;background:linear-gradient(180deg,#5d93d4 0%,#9cc1e6 30%,#3a3a44 55%,#3b3a3a 75%,#e9e9e9 82%,#a79a73 100%)"></div>
  <div class="abs partner-corner"></div>
  <div class="abs partner-strip"></div>

  <div class="abs event-mark"><i></i>2025 ORV K7R Global Skycup</div>

  <div class="abs cover-block"></div>
  <div class="abs rule" style="left:441px;top:122px;width:172px"></div>
  <h1 class="abs cover-title">Fueling the Future of Aeromodeling: Sponsor the 2025 K7R Global Skycup</h1>
  <div class="abs date-box">August 9–16, 2025 | ISF Headquarters, Muncie, Indiana</div>

  <div class="abs partners"><span>ISF</span><span>ORV</span><span>FGRSP</span></div>
</section>

<!-- Inside spread -->
<section class="spread spread--inside">
  <div class="abs intro-block"></div>
  <p class="abs tagline">A celebration of precision aerobatics, global talent, and cutting-edge technology.</p>
  <div class="abs heading-box overview-box"><h2 class="panel-heading">Event Overview</h2></div>

  <ul class="abs dots overview-list">
    <li><b>What:</b> The 2025 ORV K7R Global Skycup for Aerobatic Model Aircraft.</li>
    <li><b>When:</b> August 9–16, 2025.</li>
    <li><b>Where:</b> Institute for Scale Flightcraft (ISF) Headquarters, Muncie, Indiana.</li>
    <li><b>Hosted By:</b> Institute for Scale Flightcraft (ISF) in partnership with the Federated Guild for Remote Stunt Piloting (FGRSP).</li>
    <li><b>Participants:</b> Top pilots from across the globe, including juniors and female competitors.</li>
  </ul>

  <div class="photo" role="img" aria-label="Row of pilots holding colourful aerobatic model planes at sunset" style="left:0;top:369px;width:205px;height:105px;background:linear-gradient(180deg,#8fb0d8 0%,#c9d6e3 35%,#c85a4a 60%,#4a4a3c 100%)"></div>

  <h2 class="abs why-title">Why Sponsor?</h2>
  <div class="abs rule" style="left:205px;top:139px;width:140px"></div>

  <div class="abs why" style="top:172px">
    <h3>SHAPING THE FUTURE WORKFORCE:</h3>
    <p style="margin-top:10px">Inspire youth to connect their hobbies to future careers in aerospace, aviation, and high-tech industries such as Corvane and Halbrook Teller.</p>
  </div>
  <div class="abs why" style="top:255px">
    <h3>BRAND VISIBILITY:</h3>
    <p style="margin-top:10px">Be ready for the stimulating tracks to climb one of the tropical mountains on the island – Mount Larana – to be rewarded with the breathtaking sunrise from the peak</p>
  </div>
  <div class="abs why" style="top:337px">
    <h3>COMMUNITY IMPACT:</h3>
    <p style="margin-top:10px">Support an event that promotes innovation, STEM education, and cultural exchange.</p>
  </div>
  <p class="abs why-note">Your sponsorship makes a lasting impact on the future of aviation and technology.</p>
  <div class="abs red-foot"></div>

  <div class="photo" role="img" aria-label="Team group at the flying field with flag banners and model aircraft" style="left:409px;top:0;width:204px;height:139px;background:linear-gradient(180deg,#3f78c4 0%,#86b0de 45%,#e6e6e6 65%,#6f6a50 100%)"></div>
  <div class="abs features-box"><h2 class="panel-heading">Key Features of the Event</h2></div>

  <ul class="abs dots feature-list">
    <li><b>Cutting-Edge Venue:</b> Over 1,100 acres of flying space designed for precision aerobatics.</li>
    <li><b>Diverse Competitions:</b> Featuring junior and female classifications alongside world-class competitors.</li>
    <li><b>Global Audience:</b> Extensive media coverage, live streams, and on-site spectators.</li>
  </ul>

  <div class="abs stem-block"></div>
  <h2 class="abs stem-title">STEM and Industry<br>Connections</h2>
  <div class="abs rule" style="left:422px;top:345px;width:191px"></div>
  <ul class="abs dots stem-list">
    <li>Showcase how aeromodelling leads to careers in aviation, engineering, and defense.</li>
    <li>Collaborate with sponsors on outreach programs for local schools and universities.</li>
  </ul>
  <p class="abs stem-note">Partner with us to inspire innovation and connect with future industry leaders.</p>
</section>

</body>
</html>
```